KV PowerPoint Design

I need a slick PowerPoint template following my newly designed logo (see the attached ZIP file for logo details, fonts, and colors).
Please also see the Sample.pptx file for an idea of the simplicity and slickness I am after (do not consider the colors or fonts from the Sample file, just as an idea). Other ideas are very welcome.

```html
<!DOCTYPE html>
<html lang="en">
<head>
<meta charset="utf-8">
<title>KV PowerPoint Template</title>
<link rel="stylesheet" href="https://fonts.googleapis.com/css2?family=Poppins:ital,wght@0,400;0,500;0,600;0,700;0,800;1,400&display=swap">
<style>
  :root {
    --navy: #0b0b6b;
    --backdrop: #c0c0c0;
    --paper: #ffffff;
    --paper-soft: #f4f4f4;
    --ink: #6a6a78;
    --ink-soft: #8a8a96;
    --number: #c4c4c8;
    --placeholder: #858585;
    --photo-city: #8a7a5c;
    --photo-street: #5f7d54;
    --photo-studio: #ececec;
    --photo-office: #2a4a6a;
  }
  * { margin: 0; padding: 0; box-sizing: border-box; }
  html, body { width: 1200px; height: 555px; overflow: hidden; background: var(--backdrop); }
  body { position: relative; font-family: "Poppins", sans-serif; color: var(--ink); }

  .slide { position: absolute; width: 369px; height: 207px; background: var(--paper); overflow: hidden; }
  .slide > * { position: absolute; }
  .row-1 { top: 53px; }
  .row-2 { top: 283px; }
  .col-1 { left: 26px; }
  .col-2 { left: 415px; }
  .col-3 { left: 804px; }

  .navy-block { background: var(--navy); }
  .photo { display: block; }

  .brand-mark { font-weight: 800; color: var(--navy); font-size: 17px; letter-spacing: 0.5px; display: flex; align-items: center; gap: 4px; }
  .brand-mark .dot { width: 7px; height: 7px; border-radius: 50%; background: var(--navy); }

  .slide-title { font-weight: 800; color: var(--navy); font-size: 14px; letter-spacing: -0.2px; line-height: 1; }
  .lead { font-size: 7.6px; line-height: 8.4px; color: var(--ink); }
  .body-copy { font-size: 4.6px; line-height: 6.9px; color: var(--ink); }

  .footer-number { font-size: 4.6px; font-weight: 700; color: var(--navy); top: 194px; left: 9px; }
  .footer-rule { height: 0; border-top: 0.6px solid var(--navy); top: 197px; }
  .footer-url { font-size: 4.6px; letter-spacing: 0.8px; color: var(--ink); top: 194px; }
  .on-navy { color: var(--paper) !important; border-color: var(--paper) !important; }

  /* Cover */
  .cover { background: var(--paper-soft); }
  .cover-title { font-weight: 800; color: var(--paper); font-size: 24.5px; line-height: 25px; letter-spacing: 0.2px; }
  .cover-contact { font-size: 7px; font-weight: 600; color: #fafafa; line-height: 8px; text-align: center; }
  .cover-contact small { display: block; font-size: 4.2px; font-weight: 400; letter-spacing: 0.5px; line-height: 5px; }

  /* Agenda */
  .agenda-item { left: 33px; display: flex; gap: 10px; }
  .agenda-number { font-size: 14px; font-weight: 700; color: var(--number); line-height: 14px; width: 18px; }
  .agenda-head { font-size: 7.2px; font-weight: 700; color: var(--navy); line-height: 9px; }
  .agenda-copy { font-size: 4.6px; line-height: 6.9px; color: var(--ink); margin-top: 1px; }
  .quote-small { font-size: 7.3px; font-style: italic; color: var(--paper); text-align: right; line-height: 8.4px; }

  /* Team */
  .member-photo { width: 52px; height: 52px; background: var(--placeholder); top: 101px; }
  .member-info { top: 102px; width: 48px; }
  .member-name { font-size: 7.2px; font-weight: 700; color: var(--navy); line-height: 9px; }
  .member-copy { font-size: 4.6px; line-height: 6.9px; color: var(--ink); margin-top: 2px; }
  .member-phone { font-size: 4.6px; color: var(--ink); margin-top: 7px; }

  /* Bullets */
  .bullet-list { list-style: none; left: 30px; top: 82px; width: 112px; }
  .bullet-list li { position: relative; padding-left: 7px; font-size: 4.6px; line-height: 6.9px; color: var(--ink); margin-bottom: 6.2px; }
  .bullet-list li::before { content: ""; position: absolute; left: 0; top: 2.2px; width: 2.6px; height: 2.6px; border-radius: 50%; background: var(--number); }

  /* Closing */
  .closing-quote { font-size: 7.5px; font-style: italic; color: var(--paper); text-align: center; line-height: 8.3px; left: 40px; width: 288px; top: 105px; }
</style>
</head>
<body>

<!-- Cover -->
<section class="slide cover row-1 col-1">
  <div class="navy-block" style="left:299px;top:0;width:70px;height:207px;"></div>
  <svg class="photo" style="left:191px;top:16px;" width="161" height="176" role="img" aria-label="Photo of three business people in suits standing with arms crossed in front of an office building">
    <defs><linearGradient id="cover-photo" x1="0" y1="0" x2="1" y2="1"><stop offset="0" stop-color="#a9946a"/><stop offset="0.5" stop-color="#7d6a52"/><stop offset="1" stop-color="#2d2a2c"/></linearGradient></defs>
    <rect width="161" height="176" fill="url(#cover-photo)"/>
  </svg>
  <div class="navy-block" style="left:0;top:78px;width:223px;height:66px;"></div>
  <h1 class="cover-title" style="left:20px;top:87px;">BUSINESS<br>PRESENTATION</h1>
  <div class="brand-mark" style="left:17px;top:26px;"><span class="dot"></span>KV</div>
  <p class="cover-contact" style="left:118px;top:180px;">+123 456 789<small>WWW.COMPANYNAME.COM</small></p>
</section>

<!-- Intro -->
<section class="slide row-1 col-2">
  <svg class="photo" style="left:0;top:0;" width="187" height="207" role="img" aria-label="Photo of a young woman in a beige blazer holding a blue folder outside a glass office building, trees behind">
    <defs><linearGradient id="street-photo" x1="0" y1="0" x2="1" y2="0"><stop offset="0" stop-color="#4f7a3e"/><stop offset="0.55" stop-color="#c9b59b"/><stop offset="1" stop-color="#4d6a80"/></linearGradient></defs>
    <rect width="187" height="207" fill="url(#street-photo)"/>
  </svg>
  <div class="navy-block" style="left:80px;top:0;width:107px;height:68px;"></div>
  <div class="navy-block" style="left:0;top:144px;width:80px;height:31px;"></div>
  <div style="left:0;top:175px;width:80px;height:32px;background:var(--paper);"></div>
  <h2 class="slide-title" style="left:206px;top:85px;">TITLE SLIDE</h2>
  <p class="lead" style="left:206px;top:108px;width:150px;">Lorem ipsum dolor sit amet, consectetur adipiscing elit.</p>
  <p class="body-copy" style="left:206px;top:128px;width:135px;">Lorem ipsum dolor sit amet, consectetur adipiscing elit. Mauris consectetur, quam at sagittis malesuada, ex justo luctus arcu, vitae tempor risus odio eu ipsum. Phasellus mauris tortor, lobortis sit amet ex eu, dictum venenatis libero. Mauris risus velit, bibendum in rhoncus sit amet, rhoncus vel sem.</p>
  <span class="footer-number">01.</span>
  <div class="footer-rule" style="left:22px;width:256px;"></div>
  <span class="footer-url" style="left:285px;">WWW.COMPANYNAME.COM</span>
</section>

<!-- Agenda -->
<section class="slide row-1 col-3">
  <svg class="photo" style="left:185px;top:0;" width="184" height="122" role="img" aria-label="Photo of a smiling woman in a white shirt and tie holding a stack of books with a red ribbon">
    <defs><linearGradient id="studio-photo" x1="0" y1="0" x2="1" y2="0"><stop offset="0" stop-color="#f3f3f3"/><stop offset="0.7" stop-color="#e6e6e6"/><stop offset="1" stop-color="#c9a87c"/></linearGradient></defs>
    <rect width="184" height="122" fill="url(#studio-photo)"/>
  </svg>
  <div class="navy-block" style="left:270px;top:122px;width:99px;height:85px;"></div>
  <h2 class="slide-title" style="left:33px;top:26px;">TITLE SLIDE</h2>
  <div class="agenda-item" style="top:57px;"><span class="agenda-number">01.</span><div><p class="agenda-head">Lorem ipsum dolor sit</p><p class="agenda-copy">Lorem ipsum dolor sit amet,<br>consectetur adipiscing elit. Mauris</p></div></div>
  <div class="agenda-item" style="top:95px;"><span class="agenda-number">02.</span><div><p class="agenda-head">Lorem ipsum dolor sit</p><p class="agenda-copy">Lorem ipsum dolor sit amet,<br>consectetur adipiscing elit. Mauris</p></div></div>
  <div class="agenda-item" style="top:132px;"><span class="agenda-number">03.</span><div><p class="agenda-head">Lorem ipsum dolor sit</p><p class="agenda-copy">Lorem ipsum dolor sit amet,<br>consectetur adipiscing elit. Mauris</p></div></div>
  <p class="quote-small" style="left:280px;top:137px;width:80px;">Lorem ipsum dolor sit amet, consectetur adipiscing elit.</p>
  <span class="footer-number">02.</span>
  <div class="footer-rule" style="left:22px;width:248px;"></div>
  <span class="footer-url on-navy" style="left:286px;">WWW.COMPANYNAME.COM</span>
</section>

<!-- Team -->
<section class="slide row-2 col-1">
  <h2 class="slide-title" style="left:33px;top:35px;">TITLE SLIDE</h2>
  <p class="lead" style="left:33px;top:58px;width:110px;">Lorem ipsum dolor sit amet, consectetur adipiscing elit.</p>
  <p class="body-copy" style="left:199px;top:58px;width:140px;">Lorem ipsum dolor sit amet, consectetur adipiscing elit. Mauris consectetur, quam at sagittis malesuada, ex justo luctus arcu, vitae tempor risus odio eu ipsum. Phasellus</p>
  <div class="member-photo" style="left:14px;"></div>
  <div class="member-info" style="left:75px;"><p class="member-name">Jhon Doe</p><p class="member-copy">Lorem ipsum dolor sit amet, consectetur</p><p class="member-phone">+123 456 789</p></div>
  <div class="member-photo" style="left:131px;"></div>
  <div class="member-info" style="left:192px;"><p class="member-name">Jhon Doe</p><p class="member-copy">Lorem ipsum dolor sit amet, consectetur</p><p class="member-phone">+123 456 789</p></div>
  <div class="member-photo" style="left:247px;"></div>
  <div class="member-info" style="left:308px;"><p class="member-name">Jhon Doe</p><p class="member-copy">Lorem ipsum dolor sit amet, consectetur</p><p class="member-phone">+123 456 789</p></div>
  <div class="navy-block" style="left:0;top:179px;width:249px;height:28px;"></div>
  <span class="footer-number on-navy">03.</span>
  <div class="footer-rule on-navy" style="left:22px;width:227px;"></div>
  <span class="footer-url" style="left:287px;">WWW.COMPANYNAME.COM</span>
</section>

<!-- Bullets -->
<section class="slide row-2 col-2">
  <h2 class="slide-title" style="left:28px;top:35px;">TITLE SLIDE</h2>
  <p class="lead" style="left:28px;top:58px;width:110px;">Lorem ipsum dolor sit amet, consectetur adipiscing elit.</p>
  <ul class="bullet-list">
    <li>Lorem ipsum dolor sit amet, consectetur adipiscing elit.</li>
    <li>Mauris consectetur, quam at sagittis malesuada, ex justo luctus arcu.</li>
    <li>Nulla porta, arcu id euismod dictum, nunc elit molestie orci, eget molestie lacus.</li>
    <li>Phasellus mauris tortor, lobortis sit amet ex eu, dictum venenatis libero.</li>
  </ul>
  <div class="navy-block" style="left:0;top:165px;width:187px;height:42px;"></div>
  <svg class="photo" style="left:187px;top:0;" width="182" height="207" role="img" aria-label="Photo of a curly-haired woman in a blue sweater holding a tablet with charts and a coffee cup in an office">
    <defs><linearGradient id="office-photo" x1="0" y1="0" x2="1" y2="1"><stop offset="0" stop-color="#5b7a8c"/><stop offset="0.5" stop-color="#3a4f63"/><stop offset="1" stop-color="#1f4fa8"/></linearGradient></defs>
    <rect width="182" height="207" fill="url(#office-photo)"/>
  </svg>
  <span class="footer-number on-navy">02.</span>
  <div class="footer-rule on-navy" style="left:22px;width:256px;"></div>
  <span class="footer-url on-navy" style="left:285px;">WWW.COMPANYNAME.COM</span>
</section>

<!-- Closing -->
<section class="slide row-2 col-3">
  <div class="navy-block" style="left:14px;top:12px;width:340px;height:183px;"></div>
  <div style="left:160px;top:12px;width:47px;height:70px;background:var(--paper);"></div>
  <div class="brand-mark" style="left:167px;top:42px;font-size:14px;"><span class="dot" style="width:5px;height:5px;"></span>KV</div>
  <p class="closing-quote">Lorem ipsum dolor sit amet, consectetur adipiscing elit. Mauris consectetur, quam at sagittis malesuada, ex justo luctus arcu, vitae tempor risus odio eu ipsum. Phasellus mauris tortor, lobortis sit amet ex eu, dictum venenatis libero.<br>Mauris risus velit</p>
</section>

</body>
</html>
```